Tariq Goldsmiths Stationary Contest

Pakistan’s largest Jewellery, Diamond and luxury watches store requires professional stationery. We have a long list of are trusted clients since 1959, our third generation has successfully maintained and sustained the legacy and excellence in the sector.

We require stationery template as part of this contest. The stationery can be double sided.

We prefer a design that makes use of some of the premium business stationery printing options, such as foil stamping, embossing/debossing, painted edges, spot UV etc (doesn't have to use all these options, only what you feel works, but we are looking for a design that stands out and is memorable and these nice touches have that effect.)

We want an eye catching, innovative, high end professional looking stationery for an out of box design that blends well with our new logo (attached). We want the design to be an out of box solution, you may use any element to compliment the logo. You may consider incorporating watermark etc, highlighting our products (Gold and Diamond Jewellery in addition to Luxury watches)

Company details are as follows;

Company name: Tariq Goldsmiths
Contact Person: Farhan Qureshi
Designation: Business Development Consultant
Mobile: +92 333 815 6042
Email: farhanqureshi@mailvale.com
Website: www.tariqgoldsmiths.com

Target Market(s)

Matrimonial, Elite & Businesses class, Upmarket

Font styles to use
Other font styles liked:
• Designers choice

Colors

Designer to choose colors to be used in the design.

Requirements
Must have
• Look and feel: Upmarket, innovative, Modern, Professional, graceful, Elegant, designer stuff.
Nice to have
• Unique design

```html
<!DOCTYPE html>
<html lang="en">
<head>
<meta charset="utf-8">
<title>Tariq Goldsmiths – Business Card</title>
<link rel="stylesheet" href="https://fonts.googleapis.com/css2?family=Open+Sans:wght@400;700&display=swap">
<style>
  :root {
    --backdrop: #3a322d;
    --card: #141414;
    --card-edge: #0b0b0b;
    --gold: #e0a62c;
    --ink-light: #f2f2f2;
  }
  * { margin: 0; padding: 0; box-sizing: border-box; }
  html, body { width: 1200px; height: 864px; overflow: hidden; }
  body {
    background: var(--backdrop);
    font-family: "Open Sans", Arial, sans-serif;
    position: relative;
  }
  .card {
    position: absolute;
    width: 525px;
    height: 300px;
    background: var(--card);
    border: 1px solid var(--card-edge);
    box-shadow: 0 10px 28px rgba(0,0,0,.45);
  }
  /* Front */
  .card-front { left: 50px; top: 110px; }
  .brand {
    position: absolute;
    left: 0; right: 0; top: 108px;
    text-align: center;
  }
  .brand-mark {
    display: block;
    width: 30px; height: 30px;
    margin: 0 auto 18px;
    border-radius: 50%;
    background: var(--gold);
  }
  .brand-name {
    color: var(--gold);
    font-weight: 700;
    font-size: 22px;
    letter-spacing: 2px;
    text-transform: uppercase;
  }
  .brand-web {
    margin-top: 12px;
    color: var(--ink-light);
    font-size: 13px;
    letter-spacing: 3.5px;
  }
  /* Back */
  .card-back { left: 625px; top: 420px; }
  .contact { position: absolute; left: 34px; top: 130px; }
  .contact-name {
    color: var(--gold);
    font-weight: 700;
    font-size: 17px;
    text-transform: uppercase;
  }
  .contact-role {
    color: var(--ink-light);
    font-size: 15px;
    margin-bottom: 12px;
  }
  .contact-row {
    display: flex;
    align-items: center;
    gap: 9px;
    color: var(--ink-light);
    font-size: 14px;
    line-height: 22px;
  }
  .contact-row svg { width: 11px; height: 11px; flex: none; }
  .emblem {
    position: absolute;
    right: 42px; top: 92px;
    width: 112px; height: 112px;
    border-radius: 50%;
    background: var(--gold);
  }
</style>
</head>
<body>
  <section class="card card-front">
    <div class="brand">
      <span class="brand-mark"></span>
      <div class="brand-name">Tariq Goldsmiths</div>
      <div class="brand-web">www.tariqgoldsmiths.com</div>
    </div>
  </section>

  <section class="card card-back">
    <div class="contact">
      <div class="contact-name">Farhan Qureshi</div>
      <div class="contact-role">Business Development Consultant</div>
      <div class="contact-row">
        <svg viewBox="0 0 12 12" aria-hidden="true"><rect x="3" y="0.5" width="6" height="11" rx="1" fill="none" stroke="#e0a62c" stroke-width="1.2"/><circle cx="6" cy="9.5" r=".7" fill="#e0a62c"/></svg>
        <span>+92 333 815 6042</span>
      </div>
      <div class="contact-row">
        <svg viewBox="0 0 12 12" aria-hidden="true"><rect x="0.5" y="2" width="11" height="8" fill="#e0a62c"/><path d="M0.5 2 L6 6.5 L11.5 2" fill="none" stroke="#141414" stroke-width="1"/></svg>
        <span>farhanqureshi@mailvale.com</span>
      </div>
      <div class="contact-row">
        <svg viewBox="0 0 12 12" aria-hidden="true"><circle cx="6" cy="6" r="5.5" fill="#e0a62c"/><path d="M6 3 a2 2 0 0 1 2 2 c0 1.4-2 3.5-2 3.5 s-2-2.1-2-3.5 a2 2 0 0 1 2-2z" fill="#141414"/></svg>
        <span>www.tariqgoldsmiths.com</span>
      </div>
    </div>
    <div class="emblem"></div>
  </section>
</body>
</html>
```